Business card design needed with logo

My business is called QVM Solutions & it is targeted towards mobile equipment maintenance in the Mining and civil industry. My work involves maintenance planning and maintenance management plus also supply tradespeople on a labour hire basis. We can provide from basic shut-down machine rebuild plans to complete rebuild services supply plans and labour to anywhere in Australia. I would like to use the colours Black, Red and Grey, I had done a desgin as attached but doesn't really explain what we do and gears don't embroider well onto shirts.
Updates

I also wanted to see the something replace the gears maybe just making the QVM lettering look a bit different or put together differently 

Hello I have extended the deadline by a few extra days as I would like to update details on the front of card, details below & can be put which ever way looks good;

Neil Patton
Director
0417562938
QVM@mailbrook.com.au
www.qvmsolutions-demo.com.au

On the back of the card I would like to have the below printed;

Capable of providing, but not limited to, across Australia:
- Contract Maintenance Planning.
- Skilled Mobile Maintenance labour hire.
- New machine build specifications. 
- Plant risk assessments and inspections.
- Shut down and rebuild program planning.
- Preventative maintenance tasks, including build of materials lists, creation and review.

Target Market(s)

Contractors and companies that use small and large earthmoving and mining machines

Industry/Entity Type

Business

Contact Information for Business Card

Trading name is QVM Solutions
My name and title is
Neil Patton Director
0417 562 938
QVM@mailbrook.com.au

Logo Text

QVM

```html
<!DOCTYPE html>
<html lang="en">
<head>
<meta charset="utf-8">
<title>QVM Solutions – Business Card</title>
<link href="https://fonts.googleapis.com/css2?family=PT+Sans+Narrow:wght@400;700&display=swap" rel="stylesheet">
<style>
  :root {
    --backdrop: #a2a2a2;
    --paper: #ffffff;
    --red: #e20a17;
    --black: #0d0d0d;
    --ink: #1a1a1a;
    --grey: #9a9a9a;
    --pattern: #1c1c1c;
  }
  html, body {
    margin: 0;
    padding: 0;
    width: 1200px;
    height: 849px;
    overflow: hidden;
    background: var(--backdrop);
    font-family: "PT Sans Narrow", "Arial Narrow", sans-serif;
  }
  .card {
    position: absolute;
    top: 303px;
    width: 425px;
    height: 243px;
    border-radius: 11px;
    overflow: hidden;
    box-sizing: border-box;
  }
  .card-front { left: 146px; background: var(--paper); }
  .card-back { left: 628px; background: var(--red); border: 1.5px solid var(--black); }
  .card-shapes {
    position: absolute;
    inset: 0;
    width: 100%;
    height: 100%;
  }
  .brand-mark {
    position: absolute;
    left: 25px;
    top: 6px;
    display: flex;
    align-items: center;
    gap: 8px;
  }
  .brand-name {
    font-weight: 700;
    font-size: 74px;
    line-height: 1;
    color: var(--red);
    letter-spacing: -1px;
  }
  .brand-dot {
    width: 40px;
    height: 40px;
    border-radius: 50%;
    background: var(--grey);
  }
  .trading-name {
    position: absolute;
    left: 215px;
    top: 36px;
    font-size: 25px;
    color: var(--ink);
  }
  .person {
    position: absolute;
    left: 26px;
    top: 138px;
    width: 168px;
  }
  .person-name {
    font-size: 19px;
    color: var(--ink);
    line-height: 1;
    padding-bottom: 2px;
    border-bottom: 1px solid #777;
  }
  .person-title {
    font-size: 10.5px;
    color: var(--ink);
    margin-top: 3px;
  }
  .contact {
    position: absolute;
    left: 26px;
    top: 182px;
    font-size: 11px;
    color: var(--ink);
    line-height: 16px;
  }
  .contact-row { display: flex; align-items: center; gap: 11px; }
  .contact-row svg { width: 10px; height: 10px; }
  .back-name {
    position: absolute;
    left: 165px;
    top: 98px;
    font-size: 28px;
    font-style: italic;
    color: var(--ink);
  }
</style>
</head>
<body>

<div class="card card-front">
  <svg class="card-shapes" viewBox="0 0 414 237" preserveAspectRatio="none" aria-hidden="true">
    <polygon points="350,0 414,0 414,237 270,237 379,52" fill="var(--black)"/>
    <polygon points="323,0 350,0 379,52 270,237 245,237 355,52" fill="var(--red)"/>
  </svg>
  <svg class="card-shapes" viewBox="0 0 414 237" preserveAspectRatio="none" role="img" aria-label="Outline gear pattern on black band">
    <polygon points="330,110 414,110 414,237 300,237" fill="var(--pattern)" opacity="0.6"/>
  </svg>

  <div class="brand-mark">
    <span class="brand-name">QVM</span>
    <span class="brand-dot"></span>
  </div>
  <div class="trading-name">QVM Solutions</div>

  <div class="person">
    <div class="person-name">Neil Patton</div>
    <div class="person-title">Director</div>
  </div>

  <div class="contact">
    <div class="contact-row">
      <svg viewBox="0 0 10 10" aria-hidden="true"><path d="M2 1 L4 3 L3 4 Q4 6 6 7 L7 6 L9 8 L8 9 Q4 9 1 4 Q1 2 2 1Z" fill="var(--ink)"/></svg>
      <span>0417 562 938</span>
    </div>
    <div class="contact-row">
      <svg viewBox="0 0 10 10" aria-hidden="true"><rect x="0.5" y="2" width="9" height="6" fill="var(--ink)"/><path d="M1 2.5 L5 5.5 L9 2.5" stroke="#fff" stroke-width="0.8" fill="none"/></svg>
      <span>e-mail : QVM@mailbrook.com.au</span>
    </div>
  </div>
</div>

<div class="card card-back">
  <svg class="card-shapes" viewBox="0 0 414 237" preserveAspectRatio="none" aria-hidden="true">
    <polygon points="0,0 148,0 178,52 68,237 0,237" fill="var(--black)"/>
  </svg>
  <svg class="card-shapes" viewBox="0 0 414 237" preserveAspectRatio="none" role="img" aria-label="Outline gear pattern on black panel">
    <polygon points="0,0 130,0 150,52 60,237 0,237" fill="var(--pattern)" opacity="0.6"/>
  </svg>
  <div class="back-name">QVM Solutions</div>
</div>

</body>
</html>
```